Gummy Label design for hemp company

I need a 3.25 inch wide by 4 inch tall label made to be put on bags of gummies. I will include all disclaimers that need to be there, as well as my logo. This is for our 25 mg Delta 8 gummies 20ct, but I will use the design for our entire gummy line, just editing the text. Needs to have ingredient list. Ingredients: Sugar, Inulin, Corn syrup, water, pectin, citric acid, baking soda, fruit, hemp extract.

Everything should be on one label as this is going on a sticker that will be placed on a bag.
I would like to highlight that they are vegan if possible.

• Must have the following disclaimer: "Contains Farm Bill compliant hemp extract. These statements have not been evaluated by the QVR. This product is NOT intended to treat, cure, or prevent any disease. Do not operate heavy machinery while using this product. This product may cause you to fail a drug test. Consult with your doctor before trying any new products. Do not take if pregnant or lactating. If you experience any adverse effects, discontinue use and seek advice from your physician."
• NEEDS TO SAY: "100% hemp derived" also "<.3% D9 THC"

```html
<!DOCTYPE html>
<html lang="en">
<head>
<meta charset="utf-8">
<title>Delta 8 Gummies Label</title>
<link rel="stylesheet" href="https://fonts.googleapis.com/css2?family=Alfa+Slab+One&family=Fira+Sans+Condensed:wght@600;700&family=Fira+Sans:wght@600;700&family=Catamaran:wght@500&display=swap">
<style>
  :root {
    --backdrop: #e5e5e5;
    --label-white: #ffffff;
    --hemp-green: #2e8b00;
    --leaf-green: #3da500;
    --lime: #8ee000;
    --text-green: #2a7f0a;
  }
  * { margin: 0; padding: 0; box-sizing: border-box; }
  html, body {
    width: 1009px;
    height: 1200px;
    overflow: hidden;
    background: var(--backdrop);
  }
  ul { list-style: none; }
  .label {
    position: absolute;
    left: 154px;
    top: 169px;
    width: 701px;
    height: 862px;
    background: var(--label-white);
    overflow: hidden;
  }
  .hero {
    position: absolute;
    left: 0;
    top: 0;
    width: 701px;
    height: 397px;
    background: linear-gradient(135deg, var(--hemp-green) 0%, var(--leaf-green) 45%, var(--hemp-green) 70%, var(--leaf-green) 100%);
  }
  .brand {
    position: absolute;
    right: 26px;
    top: 96px;
    display: flex;
    align-items: center;
    gap: 8px;
    font-family: "Fira Sans", sans-serif;
    font-weight: 700;
    font-size: 30px;
    color: var(--label-white);
    letter-spacing: -0.5px;
  }
  .brand-mark {
    width: 22px;
    height: 22px;
    border-radius: 50%;
    background: var(--label-white);
  }
  .product-name {
    position: absolute;
    left: 32px;
    top: 166px;
    font-family: "Alfa Slab One", serif;
    font-weight: 400;
    font-size: 146px;
    line-height: 1;
    color: var(--label-white);
    transform: scaleX(0.7);
    transform-origin: left top;
    white-space: nowrap;
  }
  .product-type {
    position: absolute;
    left: 32px;
    top: 292px;
    font-family: "Alfa Slab One", serif;
    font-weight: 400;
    font-size: 64px;
    line-height: 1;
    color: var(--label-white);
    letter-spacing: 28px;
    transform: scaleX(0.6);
    transform-origin: left top;
    white-space: nowrap;
  }
  .dose-pill {
    position: absolute;
    left: 30px;
    top: 370px;
    width: 353px;
    height: 49px;
    border-radius: 25px;
    background: var(--lime);
    color: var(--label-white);
    font-family: "Fira Sans Condensed", sans-serif;
    font-weight: 700;
    font-size: 36px;
    line-height: 49px;
    text-align: center;
    letter-spacing: -0.5px;
  }
  .ingredients {
    position: absolute;
    left: 35px;
    top: 477px;
    width: 567px;
    height: 108px;
    border: 2px solid var(--hemp-green);
    border-radius: 10px;
  }
  .ingredients-tab {
    position: absolute;
    left: 14px;
    top: -19px;
    width: 193px;
    height: 33px;
    border-radius: 17px;
    background: var(--hemp-green);
    color: var(--label-white);
    font-family: "Fira Sans Condensed", sans-serif;
    font-weight: 600;
    font-size: 22px;
    line-height: 33px;
    padding-left: 30px;
  }
  .ingredients-list {
    position: absolute;
    left: 14px;
    top: 26px;
    width: 545px;
    font-family: "Fira Sans", sans-serif;
    font-weight: 600;
    font-size: 25px;
    line-height: 36px;
    letter-spacing: -0.4px;
    color: var(--text-green);
    white-space: nowrap;
  }
  .claims {
    position: absolute;
    left: 30px;
    top: 605px;
    display: flex;
  }
  .claim {
    width: 92px;
    display: flex;
    flex-direction: column;
    align-items: center;
  }
  .claim svg { width: 62px; height: 62px; }
  .claim-name {
    margin-top: 7px;
    font-family: "Fira Sans Condensed", sans-serif;
    font-weight: 600;
    font-size: 12px;
    color: var(--lime);
    white-space: nowrap;
  }
  .compliance {
    position: absolute;
    left: 420px;
    top: 620px;
    font-family: "Fira Sans Condensed", sans-serif;
    font-weight: 700;
    font-size: 22px;
    line-height: 30px;
    color: var(--text-green);
    white-space: nowrap;
  }
  .disclaimer {
    position: absolute;
    left: 32px;
    top: 705px;
    width: 645px;
    font-family: "Catamaran", sans-serif;
    font-weight: 500;
    font-size: 16.5px;
    line-height: 21.6px;
    color: var(--text-green);
    white-space: nowrap;
  }
</style>
</head>
<body>
  <main class="label">
    <div class="hero" role="img" aria-label="Green background with large hemp leaf silhouettes"></div>

    <div class="brand"><span class="brand-mark"></span>Sunny Leaf Hemp</div>

    <h1 class="product-name">DELTA 8</h1>
    <p class="product-type">GUMMIES</p>
    <p class="dose-pill">25MG PER GUMMY</p>

    <section class="ingredients">
      <h2 class="ingredients-tab">INGREDIENTS</h2>
      <p class="ingredients-list">Sugar, Inulin, Corn syrup, water, pectin,<br>citric acid, baking soda, fruit, hemp extract.</p>
    </section>

    <ul class="claims">
      <li class="claim">
        <svg viewBox="0 0 62 62" aria-hidden="true">
          <circle cx="31" cy="31" r="28" fill="none" stroke="var(--lime)" stroke-width="4"/>
          <line x1="31" y1="14" x2="31" y2="52" stroke="var(--lime)" stroke-width="3"/>
          <g fill="var(--lime)">
            <ellipse cx="25" cy="24" rx="6" ry="3" transform="rotate(30 25 24)"/>
            <ellipse cx="37" cy="24" rx="6" ry="3" transform="rotate(-30 37 24)"/>
            <ellipse cx="25" cy="33" rx="6" ry="3" transform="rotate(30 25 33)"/>
            <ellipse cx="37" cy="33" rx="6" ry="3" transform="rotate(-30 37 33)"/>
            <ellipse cx="25" cy="42" rx="6" ry="3" transform="rotate(30 25 42)"/>
            <ellipse cx="37" cy="42" rx="6" ry="3" transform="rotate(-30 37 42)"/>
            <ellipse cx="31" cy="16" rx="3" ry="6"/>
          </g>
          <line x1="12" y1="50" x2="50" y2="12" stroke="var(--lime)" stroke-width="4"/>
        </svg>
        <span class="claim-name">GLUTEN FREE</span>
      </li>
      <li class="claim">
        <svg viewBox="0 0 62 62" aria-hidden="true">
          <circle cx="31" cy="31" r="28" fill="none" stroke="var(--lime)" stroke-width="4"/>
          <path d="M27 14h8M28 14v12l-9 18h24l-9-18V14" fill="none" stroke="var(--lime)" stroke-width="3" stroke-linejoin="round"/>
          <path d="M22 38h18l3 6H19z" fill="var(--lime)"/>
          <line x1="12" y1="50" x2="50" y2="12" stroke="var(--lime)" stroke-width="4"/>
        </svg>
        <span class="claim-name">CHEMICAL FREE</span>
      </li>
      <li class="claim">
        <svg viewBox="0 0 62 62" aria-hidden="true">
          <circle cx="31" cy="31" r="28" fill="none" stroke="var(--lime)" stroke-width="4"/>
          <path d="M30 42C18 42 14 32 14 24c9 0 16 4 16 18z" fill="var(--lime)"/>
          <path d="M32 42c0-13 8-20 18-20 0 10-6 20-18 20z" fill="var(--lime)"/>
          <path d="M31 46v-6" stroke="var(--lime)" stroke-width="3"/>
        </svg>
        <span class="claim-name">VEGAN</span>
      </li>
      <li class="claim">
        <svg viewBox="0 0 62 62" aria-hidden="true">
          <circle cx="31" cy="31" r="28" fill="none" stroke="var(--lime)" stroke-width="4"/>
          <clipPath id="flag-clip"><circle cx="31" cy="31" r="24"/></clipPath>
          <g clip-path="url(#flag-clip)" fill="var(--lime)">
            <rect x="5" y="7" width="52" height="4"/>
            <rect x="5" y="15" width="52" height="4"/>
            <rect x="5" y="23" width="52" height="4"/>
            <rect x="5" y="31" width="52" height="4"/>
            <rect x="5" y="39" width="52" height="4"/>
            <rect x="5" y="47" width="52" height="4"/>
            <rect x="5" y="7" width="24" height="20"/>
          </g>
        </svg>
        <span class="claim-name">USA ORIGIN</span>
      </li>
    </ul>

    <p class="compliance">100% HEMP DERIVED<br>&lt;.3% D9 THC</p>

    <p class="disclaimer">Contains Farm Bill compliant hemp extract. These statements have not been evaluated<br>by the QVR. This product is NOT intended to treat, cure, or prevent any disease. Do not<br>operate heavy machinery while using this product. This product may cause you to fail<br>a drug test. Consult with your doctor before trying any new products. Do not take if<br>pregnant or lactating. If you experience any adverse effects, discontinue use and seek<br>advice from your physician.</p>
  </main>
</body>
</html>
```